Webdesign für IT-Beratungsdienstleister
Zielgruppe
7K-ADVISA ist spezialisiert auf Fach- und IT-Beratungsdienstleistungen.
Wir unterstützen Unternehmen bei der Leistungsoptimierung durch prozessgetriebene Informationssysteme und Integrationslösungen.
Bitte siehe Aufgaben hier: http://www.7k-advisa.example/ueber-uns/
Zielgruppe sind Mittelständige und sowie Grossunternehmen
Aufgabenstellung
Wordpress template, modern, nicht zu überladen mit der Möglichkeit Beiträge zu veröffentlicehn. Responsive.

```html
<!DOCTYPE html>
<html lang="de">
<head>
<meta charset="utf-8">
<title>7K-ADVISA – Fach- und IT-Beratung</title>
<link rel="stylesheet" href="https://fonts.googleapis.com/css2?family=Ubuntu:ital,wght@0,300;0,400;0,500;0,700;1,400&family=Roboto:wght@400&display=swap">
<style>
:root{
  --orange:#e8650f;
  --orange-light:#f07a2a;
  --blue:#0b6fc5;
  --blue-light:#0e8fe0;
  --green:#00b04f;
  --green-light:#08d95c;
  --red:#f0200f;
  --ink:#333a44;
  --muted:#777;
  --panel:#ececec;
  --light:#f2f2f2;
  --slate:#434c5e;
  --footer:#2b3340;
  --white:#fff;
}
*{box-sizing:border-box;margin:0;padding:0}
html,body{width:1200px;height:2434px;overflow:hidden}
body{position:relative;font-family:'Ubuntu',sans-serif;color:var(--ink);background:var(--white)}
.abs{position:absolute}
ul{list-style:none}

/* header */
.site-header{left:0;top:0;width:1200px;height:63px;background:var(--white);border-bottom:1px solid #ddd}
.brand{left:246px;top:12px;font-size:32px;font-weight:400;color:var(--ink);letter-spacing:1px}
.main-nav{right:185px;top:21px;display:flex;gap:18px;font-family:'Roboto',sans-serif;font-size:11px;color:#666}
.main-nav a{padding:3px 7px;color:#666;text-decoration:none}
.main-nav a.active{border:1px solid var(--orange);color:var(--orange)}

/* hero */
.hero{left:0;top:63px;width:1200px;height:296px;background:linear-gradient(180deg,#5f8ea0 0%,#9cbcc2 60%,#c7d6cf 100%)}
.hero-photo{left:620px;top:63px;width:560px;height:296px;background:linear-gradient(160deg,#b06a2c 0%,#2e3a55 35%,#1f2a40 100%);opacity:.85}
.hero-title{left:151px;top:131px;font-size:18px;font-weight:300;color:var(--white)}
.rule{width:30px;height:2px;background:var(--red)}
.hero-text{left:151px;top:185px;width:420px;font-size:12.5px;font-weight:300;color:var(--white);line-height:1.15}
.btn-outline{border:1.5px solid var(--white);color:var(--white);font-size:9px;font-weight:500;text-align:center}
.dots{left:579px;top:339px;display:flex;gap:4px}
.dots span{width:7px;height:7px;border-radius:50%;background:#222;border:1px solid #fff}
.dots span:first-child{background:#fff}

/* about */
.about{left:0;top:359px;width:1200px;height:302px;background:linear-gradient(90deg,#343b4a 0%,var(--slate) 50%,#5a6478 100%)}
.about-title{left:548px;top:421px;font-size:18px;font-weight:300;color:var(--white)}
.about-text{left:548px;top:473px;width:410px;font-size:12px;font-weight:300;color:var(--white);line-height:1.4}

/* services */
.service{top:706px;width:240px;height:276px;background:var(--panel)}
.service-head{height:53px;color:var(--white);font-weight:700;font-size:15px;text-align:center;line-height:53px}
.service-sub{height:64px;color:var(--white);font-weight:700;font-size:8px;text-align:center;padding:25px 8px 0;line-height:1.5;position:relative}
.service-sub::after{content:"";position:absolute;left:110px;bottom:-10px;border:10px solid transparent;border-bottom:0;border-top-color:inherit}
.service ul{padding:40px 0 0 24px;font-size:9.5px;color:#444;line-height:16px}
.service li::before{content:"•";margin-right:5px}
.svc-business{left:241px;border:1px solid var(--orange)}
.svc-business .service-head{background:var(--orange)}
.svc-business .service-sub{background:var(--orange-light);border-top-color:var(--orange-light)}
.svc-it{left:481px;border:1px solid var(--blue-light)}
.svc-it .service-head{background:var(--blue)}
.svc-it .service-sub{background:var(--blue-light);border-top-color:var(--blue-light)}
.svc-coach{left:720px;border:1px solid var(--green-light)}
.svc-coach .service-head{background:var(--green)}
.svc-coach .service-sub{background:var(--green-light);border-top-color:var(--green-light)}

/* process */
.process-brand{left:241px;top:1015px;width:232px;height:82px;background:var(--red);color:var(--white);font-size:22px;padding:22px 0 0 24px;clip-path:polygon(0 0,100% 0,94% 100%,0 100%)}
.process-steps{left:458px;top:1009px;width:502px;height:96px}
.step{top:1050px;font-size:10.5px;font-weight:700;color:#333}

/* articles */
.articles{left:0;top:1167px;width:1200px;height:381px;background:var(--light)}
.articles-title{left:0;top:1203px;width:1200px;text-align:center;font-size:18px;font-weight:300}
.articles-rule{left:585px;top:1236px}
.arrows{left:938px;top:1256px;font-size:11px;color:var(--orange)}
.card{top:1272px;width:227px}
.card-img{height:129px;background:linear-gradient(135deg,#5b6372 0%,#2d323c 55%,#8a6a4a 100%);border:1px solid #999}
.read-more{position:absolute;left:-7px;top:99px;background:var(--red);color:#fff;font-size:7px;padding:6px 8px}
.card-meta{margin-top:16px;font-size:6px;font-style:italic;color:#777}
.card-meta em{color:var(--orange)}
.card-title{margin-top:10px;font-size:9.5px;font-style:italic;color:var(--orange)}
.btn-orange{left:558px;top:1477px;width:84px;height:26px;background:var(--orange);color:#fff;font-size:8px;font-weight:700;text-align:center;line-height:26px}

/* contact */
.contact-bg{left:0;top:1548px;width:1200px;height:345px;background:linear-gradient(180deg,#7c869c 0%,#6a7080 45%,#515547 75%,#3e4636 100%)}
.contact-box{left:241px;top:1661px;width:719px;height:119px;background:var(--orange);clip-path:polygon(0 0,72% 6%,100% 8%,100% 100%,0 100%)}
.contact-title{left:272px;top:1705px;font-size:15.5px;font-weight:300;color:#fff}
.contact-sub{left:272px;top:1737px;font-size:9.5px;color:#f6c49b}
.contact-btn{left:813px;top:1718px;width:112px;height:21px;line-height:18px}

/* map */
.map{left:0;top:1893px;width:1200px;height:306px;background:linear-gradient(100deg,#fbe8dc 0%,#f6c7a6 45%,#f7d2b6 75%,#fbe6d8 100%)}

/* footer */
.footer{left:0;top:2199px;width:1200px;height:235px;background:var(--footer)}
.footer-brand{left:245px;top:2234px;font-size:23px;color:#fff}
.footer-text{left:241px;top:2280px;width:285px;font-size:7px;color:#fff;line-height:16px}
.footer-h{font-size:11px;font-weight:500;color:#fff;letter-spacing:.5px}
.footer-links{left:548px;top:2255px;font-size:7px;font-weight:500;color:#fff;line-height:16px}
.social{left:800px;top:2254px}
.social span{display:block;width:18px;height:18px;background:#14181f;margin-bottom:4px}
.footer-rule{left:241px;top:2385px;width:719px;height:3px;background:var(--red)}
.copyright{left:0;top:2408px;width:1200px;text-align:center;font-size:9px;color:#8a93a2}
.copyright b{color:#fff;font-weight:400}
</style>
</head>
<body>

<header class="abs site-header"></header>
<div class="abs brand">7K-ADVISA</div>
<nav class="abs main-nav">
  <a class="active">Home</a><a>Profil</a><a>Services</a><a>Karriere</a><a>Kontakt</a><a>Publikationen</a>
</nav>

<section class="abs hero" role="img" aria-label="Himmel mit Wolken als Hintergrund"></section>
<div class="abs hero-photo" role="img" aria-label="Berater im Anzug öffnet sein Hemd vor blauem Himmel"></div>
<h1 class="abs hero-title">7K-ADVISA - Unser Know-How für Ihren Erfolg!</h1>
<div class="abs rule" style="left:151px;top:164px"></div>
<div class="abs hero-text">Wir beraten namhafte Unternehmen und stellen individuelle Lösungen zur Verfügung.<br><br>Was dürfen wir für Sie tun?</div>
<div class="abs btn-outline" style="left:151px;top:264px;width:145px;height:23px;line-height:20px">Jetzt kontakt aufnehmen</div>
<div class="abs dots"><span></span><span></span><span></span><span></span></div>

<section class="abs about" role="img" aria-label="Büroraum mit Fensterfront, abgedunkelt"></section>
<h2 class="abs about-title">Über Uns</h2>
<div class="abs rule" style="left:548px;top:453px"></div>
<p class="abs about-text">7K-ADVISA ist spezialisiert auf Fach- und IT-Beratungsdienstleistungen. Wir unterstützen Unternehmen bei der Leistungsoptimierung durch prozessgetriebene Informationssysteme. Unsere Kunden vertrauen unseren Full-Service Ansatz, der sich durch hohe Expertise mit fundierten Branchenübergreifenden Erfahrungen sowie Kompetenzen auszeichnet.</p>
<div class="abs btn-outline" style="left:548px;top:583px;width:89px;height:27px;line-height:24px">Mehr erfahren</div>

<div class="abs service svc-business">
  <div class="service-head">Business Consulting</div>
  <div class="service-sub">Beratung zur fachlichen Prozessoptimierung sowie Business Analyse.</div>
  <ul><li>Prozessmodelierung, -analyse und -Gestaltung</li><li>Business Analyse</li><li>Anforderungsanalyse</li><li>Projektqualifizierung</li><li>BPM / Business Rules</li></ul>
</div>
<div class="abs service svc-it">
  <div class="service-head">IT Consulting</div>
  <div class="service-sub">Technologie Beratung im Bezug auf Implementierung und Management.</div>
  <ul><li>Prozessimplementierung</li><li>Enterprise Architecture</li><li>IT- Architecture</li><li>IT- und Applikationsintegration</li><li>BPM / SOA</li><li>Service Management</li></ul>
</div>
<div class="abs service svc-coach">
  <div class="service-head">Schulung / Coaching</div>
  <div class="service-sub">Unterstützung als Task-Force für den Projektlauf bzw. Qualifizierung.</div>
  <ul><li>Methodik Schulungen: BPM, BPMN</li><li>Durchführung von Proof of Concept</li><li>Coach für BPM/SOA Competence Center</li></ul>
</div>

<svg class="abs process-steps" viewBox="0 0 502 96" aria-hidden="true">
  <polygon points="14,2 500,2 486,94 0,94" fill="#fff" stroke="#ddd"/>
  <path d="M150 20 L154 48 L146 76 M272 20 L276 48 L268 76 M393 20 L397 48 L389 76" stroke="#e4e4e4" fill="none"/>
</svg>
<div class="abs process-brand">7K-ADVISA</div>
<div class="abs step" style="left:520px">Beratung</div>
<div class="abs step" style="left:616px">Projektmanagement</div>
<div class="abs step" style="left:737px">Implementierung</div>
<div class="abs step" style="left:876px">Schulung</div>

<section class="abs articles"></section>
<h2 class="abs articles-title">Letzte Artikeln</h2>
<div class="abs rule articles-rule"></div>
<div class="abs arrows">‹ ›</div>
<article class="abs card" style="left:247px">
  <div class="card-img" role="img" aria-label="Schreibtisch mit Tastatur, Telefon und Unterlagen"></div>
  <span class="read-more">Read more +</span>
  <div class="card-meta">26. November 2016 Von admin in <em>Artikeln</em></div>
  <div class="card-title">MusterArtikel</div>
</article>
<article class="abs card" style="left:487px">
  <div class="card-img" role="img" aria-label="Schreibtisch mit Tastatur, Telefon und Unterlagen"></div>
  <span class="read-more">Read more +</span>
  <div class="card-meta">26. Oktober 2016 Von admin in <em>Artikeln</em></div>
  <div class="card-title">MusterArtikel</div>
</article>
<article class="abs card" style="left:727px">
  <div class="card-img" role="img" aria-label="Schreibtisch mit Tastatur, Telefon und Unterlagen"></div>
  <span class="read-more">Read more +</span>
  <div class="card-meta">26. September 2016 Von admin in <em>Artikeln</em></div>
  <div class="card-title">MusterArtikel</div>
</article>
<div class="abs btn-orange">Ältere Artikeln</div>

<section class="abs contact-bg" role="img" aria-label="Stadtansicht von oben mit Fernsehturm im Dunst"></section>
<div class="abs contact-box"></div>
<h2 class="abs contact-title">Wir freuen uns immer, von Ihnen zu hören.</h2>
<p class="abs contact-sub">Inhaber und Ansprechpartner: Dr. Malik Terrano</p>
<div class="abs btn-outline contact-btn">Kontakt aufnehmen</div>

<section class="abs map" role="img" aria-label="Stadtplan mit Standortmarkierung"></section>

<footer class="abs footer"></footer>
<div class="abs footer-brand">7K-ADVISA</div>
<p class="abs footer-text">Lorem ipsum dolor sit amet, consetetur sadipscing elitr, sed diam nonumy eirmod tempor invidunt ut labore et dolore magna aliquyam erat, sed diam voluptua. At vero eos et accusam et justo duo dolores et ea rebum.</p>
<div class="abs footer-h" style="left:548px;top:2231px">Links</div>
<ul class="abs footer-links"><li>Home</li><li>Profile</li><li>Business Consulting</li><li>IT Consulting</li><li>Training</li><li>Kontakt</li><li>Publikationen</li></ul>
<div class="abs footer-h" style="left:794px;top:2231px">Soziale Netzwerke</div>
<div class="abs social"><span></span><span></span><span></span><span></span><span></span></div>
<div class="abs footer-rule"></div>
<div class="abs copyright">Copyright © 2016 7K-ADVISA. | <b>Home</b> | <b>Impressum</b> | <b>Kontakt</b></div>

</body>
</html>
```